Modern furniture store needs a catalogue in PDF

We need a catalogue design for a company based in Ecuador, South America called KOVARI. We have replica furniture and also authentic furniture from Europe which are classified in two separate ranges. KOVARI is the brand for designer replicas and THE LUMENHAUS SHOP is for authentic designer furniture and house decoration. We would like to see a design that provides an idea of exclusivity and minimalistic design.

Target Market(s)

Upmarket families and new home owners from Ecuador, South America.

Industry/Entity Type

Furniture Store

Font styles to use
Sans Serif

Requirements
Must have
• A nice presentation of each furniture item.
• You can look for images on the internet for each product as they are designer items available all around the world. You can use images from the websites:
• www.kovari-home.net
• www.pelzora.com
• www.wimsel.fi
• The images don't need to be high resolution as the PDF will be sent electronically (i.e. via email) and not printed.
Nice to have
• Diagrams with the dimensions of each item so that clients understand how big they are.
• It could be in spanish, but I could also translate it after the design is finished.

```html
<!DOCTYPE html>
<html lang="es">
<head>
<meta charset="utf-8">
<title>KOVARI — Catálogo, página 3</title>
<link href="https://fonts.googleapis.com/css2?family=Open+Sans:wght@300;400;600&display=swap" rel="stylesheet">
<style>
  :root {
    --paper: #ffffff;
    --sand: #e9e1d2;
    --sand-line: #e4dccb;
    --ink: #2e2e2e;
    --rule: #1e1e1e;
    --accent: #d5302a;
    --highlight: #ece4d5;
    --folio: #d2d2d2;
    --chrome: #d9d9d9;
  }
  * { box-sizing: border-box; margin: 0; padding: 0; }
  html, body { width: 1200px; height: 1200px; overflow: hidden; background: var(--paper); }
  .page {
    position: relative; width: 1200px; height: 1200px; overflow: hidden;
    font-family: "Open Sans", Arial, sans-serif; font-weight: 300; color: var(--ink);
  }
  .page-waves { position: absolute; inset: 0; }
  .spec-table {
    position: absolute; width: 387px; border-collapse: collapse;
    font-size: 21px; line-height: 27px;
  }
  .spec-table th {
    width: 124px; text-align: right; font-weight: 300; padding: 1px 6px 0 0;
    border-right: 1.5px solid var(--rule); vertical-align: middle; white-space: nowrap;
  }
  .spec-table td { padding: 1px 0 0 7px; white-space: nowrap; }
  .spec-table tr:not(:last-child) th,
  .spec-table tr:not(:last-child) td { border-bottom: 1.5px solid var(--rule); }
  .spec-table .item-code { color: var(--accent); font-weight: 600; }
  .spec-table .model td { background: var(--highlight); color: var(--accent); }
  .product-photo { position: absolute; border-radius: 14px; }
  .photo-black { left: 808px; top: 160px; width: 252px; height: 200px;
    background: linear-gradient(180deg, #2c302e 0%, #2c302e 40%, var(--chrome) 62%, #f4f4f4 100%); }
  .photo-white { left: 179px; top: 488px; width: 291px; height: 244px;
    background: linear-gradient(180deg, #f3f3f3 0%, #e6e6e6 40%, #a9a9a9 62%, #eeeeee 100%); }
  .photo-brown { left: 779px; top: 854px; width: 276px; height: 238px;
    background: linear-gradient(180deg, #4a2b22 0%, #4a2b22 40%, var(--chrome) 62%, #f4f4f4 100%); }
  .folio {
    position: absolute; left: 1104px; top: 1040px; font-size: 112px; font-weight: 300;
    color: var(--paper); -webkit-text-stroke: 2px var(--folio); line-height: 1;
  }
</style>
</head>
<body>
<div class="page">
  <svg class="page-waves" width="1200" height="1200" viewBox="0 0 1200 1200" aria-hidden="true">
    <path d="M0 0 H1200 V113 C1120 70 960 40 720 45 C480 50 250 70 0 42 Z" fill="var(--sand)"/>
    <path d="M0 372 C180 392 330 432 600 428 C870 424 1020 398 1200 485" fill="none" stroke="var(--sand-line)" stroke-width="4"/>
    <path d="M0 745 C180 764 330 804 600 800 C870 796 1020 772 1200 857" fill="none" stroke="var(--sand-line)" stroke-width="4"/>
  </svg>

  <table class="spec-table" style="left:267px; top:106px;">
    <tr><th>Item</th><td class="item-code">B103</td></tr>
    <tr><th>Marca</th><td>KOVARI</td></tr>
    <tr><th>Diseñador</th><td>Aurel Venholt 1929</td></tr>
    <tr class="model"><th>Modelo</th><td>Castellet Otomana</td></tr>
    <tr><th>Acabado</th><td>Acero Inox. Frente C/<br>Natural, Reves C/<br>Artificial. Esponja A/D</td></tr>
    <tr><th>Medidas</th><td>Ancho: 54 cms.<br>Fondo: 61 cms.<br>Altura: 42 cms</td></tr>
    <tr><th>Color</th><td>NEGRO</td></tr>
  </table>
  <div class="product-photo photo-black" role="img" aria-label="Otomana tapizada en cuero negro capitoneado con base de acero inoxidable en X"></div>

  <div class="product-photo photo-white" role="img" aria-label="Otomana tapizada en cuero blanco capitoneado con base de acero inoxidable en X"></div>
  <table class="spec-table" style="left:535px; top:464px;">
    <tr><th>Item</th><td class="item-code">B104</td></tr>
    <tr><th>Marca</th><td>KOVARI</td></tr>
    <tr><th>Diseñador</th><td>Aurel Venholt 1929</td></tr>
    <tr class="model"><th>Modelo</th><td>Castellet Otomana</td></tr>
    <tr><th>Acabado</th><td>Acero Inox. Frente C/<br>Natural, Reves C/<br>Artificial. Esponja A/D</td></tr>
    <tr><th>Medidas</th><td>Ancho: 54 cms.<br>Fondo: 61 cms.<br>Altura: 42 cms</td></tr>
    <tr><th>Color</th><td>BLANCO</td></tr>
  </table>

  <table class="spec-table" style="left:267px; top:849px;">
    <tr><th>Item</th><td class="item-code">B105</td></tr>
    <tr><th>Marca</th><td>KOVARI</td></tr>
    <tr><th>Diseñador</th><td>Aurel Venholt 1929</td></tr>
    <tr class="model"><th>Modelo</th><td>Castellet Otomana</td></tr>
    <tr><th>Acabado</th><td>Acero Inox. Frente C/<br>Natural, Reves C/<br>Artificial. Esponja A/D</td></tr>
    <tr><th>Medidas</th><td>Ancho: 54 cms.<br>Fondo: 61 cms.<br>Altura: 42 cms</td></tr>
    <tr><th>Color</th><td>CAFÉ</td></tr>
  </table>
  <div class="product-photo photo-brown" role="img" aria-label="Otomana tapizada en cuero café capitoneado con base de acero inoxidable en X"></div>

  <div class="folio">3</div>
</div>
</body>
</html>
```